Harbormoor Property Institute Needs Banner Designs

I just launched an online real estate school at www.harbormoorpropertyinstitute.com

I am seeking designers to work on 2 banners (listed seperately) as well as a a Facebook design. This listing is for 1 of 2 banners.

First banner I intend to use on different job offering web sites. So "Launch your career into Real Estate" could be the concept. i'm open to 1 sentence pitch's. please look at my website to view graphics and colors.

```html
<!DOCTYPE html>
<html lang="en">
<head>
<meta charset="utf-8">
<title>Launch Your Career Into Real Estate — Harbormoor Property Institute</title>
<link rel="stylesheet" href="https://fonts.googleapis.com/css2?family=Montserrat:wght@700;800;900&family=Source+Sans+3:wght@600;700&display=swap">
<style>
  :root {
    --navy: #0c3a78;
    --navy-deep: #1f3768;
    --orange: #f7941d;
    --white: #ffffff;
    --ink: #333333;
  }
  html, body {
    margin: 0;
    padding: 0;
    overflow: hidden;
    background: var(--white);
  }
  .banner {
    position: relative;
    width: 1200px;
    height: 457px;
    overflow: hidden;
    background: var(--white);
  }
  .banner__art {
    position: absolute;
    inset: 0;
  }
  .headline {
    position: absolute;
    left: 0;
    top: 0;
    width: 1200px;
    height: 170px;
    margin: 0;
    font-family: "Montserrat", sans-serif;
    line-height: 1;
  }
  .headline span {
    position: absolute;
    white-space: nowrap;
    line-height: 1;
  }
  .headline__lead {
    left: 592px;
    top: 78px;
    font-size: 27px;
    font-weight: 800;
    color: var(--ink);
  }
  .headline__focus {
    left: 818px;
    top: 44px;
    font-size: 80px;
    font-weight: 900;
    letter-spacing: -3px;
    color: var(--orange);
  }
  .headline__tail {
    right: 56px;
    top: 134px;
    font-size: 26px;
    font-weight: 800;
    color: var(--ink);
  }
  .feature {
    position: absolute;
    width: 180px;
    margin: 0 0 0 -90px;
    font-family: "Source Sans 3", sans-serif;
    font-weight: 700;
    font-size: 15px;
    line-height: 1.3;
    color: var(--white);
    text-align: center;
    white-space: nowrap;
  }
  .brand {
    position: absolute;
    left: 83px;
    top: 336px;
    width: 137px;
    height: 121px;
    background: var(--white);
    display: flex;
    flex-direction: column;
    align-items: center;
    justify-content: center;
    gap: 8px;
    font-family: "Source Sans 3", sans-serif;
    font-weight: 700;
    font-size: 15px;
    line-height: 1.15;
    color: var(--navy-deep);
    text-align: center;
  }
  .brand__dot {
    width: 14px;
    height: 14px;
    border-radius: 50%;
    background: var(--orange);
  }
</style>
</head>
<body>
<main class="banner">
  <svg class="banner__art" width="1200" height="457" viewBox="0 0 1200 457">
    <defs>
      <linearGradient id="rocketTone" x1="0" y1="0" x2="1" y2="1">
        <stop offset="0" stop-color="#ffb24a"/>
        <stop offset="1" stop-color="#f7941d"/>
      </linearGradient>
      <linearGradient id="presenterTone" x1="0" y1="0" x2="0" y2="1">
        <stop offset="0" stop-color="#e9b98f"/>
        <stop offset="0.45" stop-color="#b9a6d6"/>
        <stop offset="1" stop-color="#b07a44"/>
      </linearGradient>
    </defs>

    <polygon class="range" fill="var(--navy)"
      points="0,45 90,80 325,242 476,108 732,326 885,242 1030,378 1090,457 0,457"/>
    <polygon class="range-edge" fill="var(--navy-deep)"
      points="0,45 88,80 88,457 0,457"/>

    <polyline class="path" fill="none" stroke="var(--orange)" stroke-width="17"
      points="88,58 168,134 325,222 476,90 732,307 885,222 1060,380"/>

    <g class="connectors" stroke="var(--white)" stroke-width="1.5">
      <line x1="168" y1="134" x2="168" y2="252"/>
      <line x1="325" y1="222" x2="325" y2="360"/>
      <line x1="476" y1="90" x2="476" y2="258"/>
      <line x1="732" y1="307" x2="732" y2="375"/>
      <line x1="885" y1="222" x2="885" y2="318"/>
    </g>
    <g class="connector-ends" fill="var(--white)">
      <circle cx="168" cy="252" r="4"/>
      <circle cx="325" cy="360" r="4"/>
      <circle cx="476" cy="258" r="4"/>
      <circle cx="732" cy="375" r="4"/>
      <circle cx="885" cy="318" r="4"/>
    </g>

    <g class="milestones">
      <g><circle cx="168" cy="134" r="17" fill="var(--orange)"/><circle cx="168" cy="134" r="11" fill="var(--white)"/><circle cx="168" cy="134" r="6" fill="var(--orange)"/></g>
      <g><circle cx="325" cy="222" r="17" fill="var(--orange)"/><circle cx="325" cy="222" r="11" fill="var(--white)"/><circle cx="325" cy="222" r="6" fill="var(--orange)"/></g>
      <g><circle cx="476" cy="90" r="17" fill="var(--orange)"/><circle cx="476" cy="90" r="11" fill="var(--white)"/><circle cx="476" cy="90" r="6" fill="var(--orange)"/></g>
      <g><circle cx="732" cy="307" r="17" fill="var(--orange)"/><circle cx="732" cy="307" r="11" fill="var(--white)"/><circle cx="732" cy="307" r="6" fill="var(--orange)"/></g>
      <g><circle cx="885" cy="222" r="17" fill="var(--orange)"/><circle cx="885" cy="222" r="11" fill="var(--white)"/><circle cx="885" cy="222" r="6" fill="var(--orange)"/></g>
    </g>

    <rect class="rocket-art" role="img" aria-label="Illustration of an orange rocket launching along the path"
      x="0" y="6" width="140" height="100" rx="30" fill="url(#rocketTone)"/>

    <rect class="presenter-art" role="img" aria-label="Cartoon illustration of a student at a desk with a laptop, raising a finger"
      x="1010" y="222" width="190" height="235" rx="24" fill="url(#presenterTone)"/>
  </svg>

  <h1 class="headline">
    <span class="headline__lead">LAUNCH YOUR</span>
    <span class="headline__focus">CAREER</span>
    <span class="headline__tail">INTO REAL ESTATE</span>
  </h1>

  <p class="feature" style="left:168px; top:264px;">Train on<br>Your Schedule</p>
  <p class="feature" style="left:325px; top:370px;">Meets State License<br>Requirements</p>
  <p class="feature" style="left:476px; top:268px;">State-Approved Courses</p>
  <p class="feature" style="left:732px; top:386px;">Convenient 100%<br>Online Courses</p>
  <p class="feature" style="left:885px; top:328px;">Quick, Easy, and<br>Affordable</p>

  <div class="brand">
    <span class="brand__dot"></span>
    <span class="brand__name">Harbormoor Property Institute</span>
  </div>
</main>
</body>
</html>
```